Ringwell Lookup - Web design / template design

Hello,

I need a design for my existing site. I already have a logo that I want to use, which you can find on my site ( I can also provide different formats / larger versions ).

Please see http://www.ringwelllookup.example for details of the site.

What I need are pages with sections that can be edited, so for example, I need basic table / div content sections that I can place in the members area that can contain whatever custom content I need to put in them without the table / div design getting stretched out or skewed.

The main page, basically needs to have all of the content on the current page or room for it at least should I want to add it.

You can also see ww2.ringwelllookup.example with more info ( not a live site and me trying my best to do something, but I'm just not good at design :)

The site content for the most part needs to be actual text, rather than text on images. I will need to change this content and have it indexed by search engines, if you want, you can just put filler text in. There are exceptions of course, like maybe on the main page, if there are boxes with some static image text, that is fine.

Target Market(s)

Telephony, phone service providers, phone system users

Industry/Entity Type

It Service

Requirements
Must have
• Dynamic content capabilities.

Logo colors implemented in the site in some way.

Easy navigation ( tabs at the top are good or whatever you think ).

I will have the following sections:

1. Home
2. About us ( company info ).
3. How to / Help
4. Pricing
5. Support section.
6. Contact section
7. Singup section
8. Members section

I would like the main page to be more image / wow factor and the other pages really just need to be basic layout and places to put tables or divs with content in them. Table or div header images are for titles are ok as long as I can edit them.

Nice to have
• Sign up button placed somewhere.

plain square (social link) / plain square (social link) / plain square (social link) buttons

Should not have
• Flash or all page content in static images.

```html
<!DOCTYPE html>
<html lang="en">
<head>
<meta charset="utf-8">
<title>Ringwell Lookup – CNAM Provider</title>
<link rel="stylesheet" href="https://fonts.googleapis.com/css2?family=Noto+Sans:wght@400;700&family=Yanone+Kaffeesatz:wght@400;500&display=swap">
<style>
:root{
  --green:#2e8f0e;
  --green-bullet:#2f7a14;
  --blue:#0b74c0;
  --blue-deep:#0666ad;
  --blue-head:#1e6fcf;
  --nav:#1f5f95;
  --text:#333;
  --muted:#555;
  --page:#f3f3f1;
  --white:#fff;
  --line:#dcdcdc;
}
*{margin:0;padding:0;box-sizing:border-box}
html,body{width:1158px;height:1200px;overflow:hidden}
body{background:var(--page);font-family:"Noto Sans",sans-serif;color:var(--text);position:relative}
.site-header{position:absolute;left:0;top:0;width:1158px;height:116px;background:var(--white);border-bottom:2px solid #e2e2e2}
.brand{position:absolute;left:126px;top:50px;font-size:29px;font-weight:700;color:var(--blue-deep);letter-spacing:-.5px}
.main-nav{position:absolute;top:65px;left:0;width:1158px}
.main-nav a{position:absolute;font-size:14px;color:var(--nav);text-decoration:none}
.tagline{position:absolute;top:132px;width:1158px;text-align:center;font-family:"Yanone Kaffeesatz",sans-serif;font-weight:500;font-size:25px;color:var(--green);transform:skewX(-6deg)}
.intro{position:absolute;top:171px;left:270px;width:618px;text-align:center;font-size:10px;line-height:15px;color:#222}
.feature-card{position:absolute;top:233px;width:257px;height:182px;background:var(--white);border:1px solid #e3e3e3;border-radius:6px}
.feature-card .icon{position:absolute;left:20px;top:40px;width:64px;height:64px}
.feature-card h2{position:absolute;left:106px;top:13px;font-weight:400;font-size:18px;color:var(--green)}
.feature-card p{position:absolute;left:106px;top:49px;width:120px;font-size:11.5px;line-height:14.5px;text-align:justify;color:var(--muted)}
.btn{display:inline-block;background:linear-gradient(#fff,#eceff2);border:1px solid #c9cfd5;border-radius:3px;color:var(--nav);font-size:12px;padding:5px 13px;text-decoration:none}
.feature-card .btn{position:absolute;left:104px;top:150px}
.info-band{position:absolute;left:0;top:445px;width:1158px;height:315px;background:radial-gradient(ellipse 260px 300px at 570px 150px,#5fa8df 0%,#2a8bd0 45%,var(--blue) 80%)}
.info-col{position:absolute;top:20px;width:272px;color:var(--white)}
.info-col h3{font-weight:400;font-size:15.5px;margin-bottom:18px}
.info-col p{font-size:12px;line-height:14.5px;text-align:justify;margin-bottom:13px;color:#eef6fc}
.info-col .btn{position:absolute;left:178px;top:264px;font-size:12px}
.benefits{position:absolute;left:121px;top:791px;width:917px;height:333px;background:var(--white);border:1px solid #e3e3e3;border-radius:6px}
.benefit-col{position:absolute;top:17px;width:211px}
.benefit-col h4{height:36px;background:linear-gradient(#2f82dd,var(--blue-head));color:var(--white);font-weight:400;font-size:15.5px;line-height:36px;padding-left:21px;border-radius:2px;margin-bottom:14px}
.benefit-col ul{list-style:none}
.benefit-col li{position:relative;padding-left:27px;font-size:12px;line-height:21.4px;color:#222}
.benefit-col li::before{content:"";position:absolute;left:13px;top:7px;width:6px;height:6px;background:var(--green-bullet)}
.social{position:absolute;left:130px;top:1143px;display:flex;gap:10px}
.social a{display:block;width:31px;height:31px;border-radius:4px;background:linear-gradient(#6ba8d8,#2f6fa8)}
.copyright{position:absolute;right:121px;top:1157px;font-size:10px;color:var(--green-bullet);letter-spacing:.3px}
</style>
</head>
<body>
<header class="site-header">
  <div class="brand">Ringwell Lookup</div>
  <nav class="main-nav">
    <a href="#" style="left:519px">Home</a>
    <a href="#" style="left:618px">About us</a>
    <a href="#" style="left:738px">CNAM Help</a>
    <a href="#" style="left:872px">Pricing</a>
    <a href="#" style="left:976px">Sing Up</a>
  </nav>
</header>

<h1 class="tagline">CNAM Provider For VoIP Based Phone Systems - Get Caller Name On Your Inbound VoIP Calls</h1>
<p class="intro">Welcome to RingwellLookup.example. It is a long established fact that a reader will be distracted by the readable content of a page when looking at its layout. The point of using Lorem .</p>

<section class="feature-card" style="left:172px">
  <div class="icon" role="img" aria-label="Two support people figures" style="background:radial-gradient(circle at 40% 45%,#8fe07a,#3b9fd8 70%);border-radius:50%"></div>
  <h2>Support</h2>
  <p>Contrary to popular belief, Lorem Ipsum is not simply random text.Lorem Ipsum is not simply random text.</p>
  <a class="btn" href="#">Read More</a>
</section>
<section class="feature-card" style="left:449px">
  <svg class="icon" viewBox="0 0 64 64" aria-hidden="true">
    <defs><radialGradient id="phoneBg" cx="40%" cy="35%" r="65%"><stop offset="0" stop-color="#8fd3f7"/><stop offset="1" stop-color="#1487cf"/></radialGradient></defs>
    <circle cx="32" cy="32" r="31" fill="url(#phoneBg)"/>
    <path d="M24 17c-3 2-5 5-4 10 2 9 9 18 17 21 4 1 7 0 9-3l-6-6-4 3c-4-2-8-7-9-11l3-4z" fill="#fff"/>
  </svg>
  <h2>Contact Us</h2>
  <p>Contrary to popular belief, Lorem Ipsum is not simply random text.Lorem Ipsum is not simply random text.</p>
  <a class="btn" href="#">Read More</a>
</section>
<section class="feature-card" style="left:724px">
  <div class="icon" role="img" aria-label="Padlock with key" style="background:linear-gradient(#e8d9a8,#b89a52);border-radius:10px"></div>
  <h2>Members Login</h2>
  <p>Contrary to popular belief, Lorem Ipsum is not simply random text.Lorem Ipsum is not simply random text.</p>
  <a class="btn" href="#">Read More</a>
</section>

<section class="info-band">
  <article class="info-col" style="left:131px">
    <h3>About RingwellLookup.example</h3>
    <p>RingwellLookup.example is a leading provider of CNAM / Caller ID Name services for VoIP providers and PBX systems. We support United States and Canadian phone numbers.</p>
    <p>We have access to all of the major CNAM databases in the United States and Canada, something we're proud to offer.</p>
    <p>Use our easy to use examples to begin delivering caller ID name to your PBX or VoIP customers in minutes.</p>
    <a class="btn" href="#">Read More</a>
  </article>
  <article class="info-col" style="left:439px">
    <h3>What is CNAM?</h3>
    <p>RingwellLookup.example is a leading provider of CNAM / Caller ID Name services for VoIP providers and PBX systems. We support United States and Canadian phone numbers.</p>
    <p>We have access to all of the major CNAM databases in the United States and Canada, something we're proud to offer.</p>
    <p>Use our easy to use examples to begin delivering caller ID name to your PBX or VoIP customers in minutes.</p>
    <a class="btn" href="#">Read More</a>
  </article>
  <article class="info-col" style="left:741px">
    <h3>How can RingwellLookup.example Help?</h3>
    <p>RingwellLookup.example is a leading provider of CNAM / Caller ID Name services for VoIP providers and PBX systems. We support United States and Canadian phone numbers.</p>
    <p>We have access to all of the major CNAM databases in the United States and Canada, something we're proud to offer.</p>
    <p>Use our easy to use examples to begin delivering caller ID name to your PBX or VoIP customers in minutes.</p>
    <a class="btn" href="#">Read More</a>
  </article>
</section>

<section class="benefits">
  <div class="benefit-col" style="left:11px">
    <h4>Why Ringwell Lookup?</h4>
    <ul><li>Realtime CNAM Dips.</li><li>No Monthly Fees.</li><li>Low Query Rates.</li><li>Free Support.</li><li>U.S. and Canadian CNAM</li><li>No Account Minimums.</li><li>Integration Assistance.</li><li>Extensive Compatablity.</li><li>High Quality Results.</li><li>Automatic Volume Discounts.</li><li>10 Daily CNAM updates.</li><li>Free, Instant Account Setup.</li></ul>
  </div>
  <div class="benefit-col" style="left:236px">
    <h4>Compatability</h4>
    <ul><li>Realtime CNAM Dips.</li><li>No Monthly Fees.</li><li>Low Query Rates.</li><li>Free Support.</li><li>U.S. and Canadian CNAM</li><li>No Account Minimums.</li><li>Integration Assistance.</li><li>Extensive Compatablity.</li><li>High Quality Results.</li><li>Automatic Volume Discounts.</li><li>10 Daily CNAM updates.</li><li>Free, Instant Account Setup.</li></ul>
  </div>
  <div class="benefit-col" style="left:462px">
    <h4>Quality and Service</h4>
    <ul><li>Realtime CNAM Dips.</li><li>No Monthly Fees.</li><li>Low Query Rates.</li><li>Free Support.</li><li>U.S. and Canadian CNAM</li><li>No Account Minimums.</li><li>Integration Assistance.</li><li>Extensive Compatablity.</li><li>High Quality Results.</li><li>Automatic Volume Discounts.</li><li>10 Daily CNAM updates.</li><li>Free, Instant Account Setup.</li></ul>
  </div>
  <div class="benefit-col" style="left:689px">
    <h4>Implementation Help</h4>
    <ul><li>Realtime CNAM Dips.</li><li>No Monthly Fees.</li><li>Low Query Rates.</li><li>Free Support.</li><li>U.S. and Canadian CNAM</li><li>No Account Minimums.</li><li>Integration Assistance.</li><li>Extensive Compatablity.</li><li>High Quality Results.</li><li>Automatic Volume Discounts.</li><li>10 Daily CNAM updates.</li><li>Free, Instant Account Setup.</li></ul>
  </div>
</section>

<footer>
  <div class="social">
    <a href="#" role="img" aria-label="Social network link"></a>
    <a href="#" role="img" aria-label="Social network link"></a>
    <a href="#" role="img" aria-label="Social network link"></a>
  </div>
  <p class="copyright">[ Copyright 2011 RingwellLookup.example | Brought to you by BrightLine ]</p>
</footer>
</body>
</html>
```